Home page graphic design only (NOT WEBSITE DESIGN)

I require a home page to be designed for my new website.
I DO NOT REQUIRE to build a website. We are a rug company specialising in alpaca wool. It is targeted at the high end of the market and hence the graphics of our page requires to reflect this. Our current page is as per attachment and I think it is too basic.
Updates

Target Market(s)

Extremly high net worth individuals where luxury is a requirement

Requirements
Must have
• show of style, luxury, uniqueness. Prefer having bright images.
Nice to have
• a highly sofisticated roomscape where the focus in the rug. See attachment as an example
Should not have
• Not sure

```html
<!DOCTYPE html>
<html lang="en">
<head>
<meta charset="utf-8">
<title>Lune Douce — Luxury Alpaca Rugs</title>
<link rel="stylesheet" href="https://fonts.googleapis.com/css2?family=Playfair+Display:ital,wght@0,400;1,400&family=Work+Sans:wght@400;600&display=swap">
<style>
  :root {
    --ink: #000000;
    --gold: #f0b92b;
    --sand: #d8bd85;
    --muted-gold: #cbb07c;
    --white: #ffffff;
    --divider: #6b5a3c;
  }
  html, body {
    margin: 0;
    padding: 0;
    overflow: hidden;
    background: var(--ink);
  }
  .home {
    position: relative;
    width: 1200px;
    height: 741px;
    background: var(--ink);
    overflow: hidden;
  }
  .brand-column {
    position: absolute;
    left: 0;
    top: 0;
    width: 534px;
    height: 741px;
    text-align: center;
  }
  .brand-name {
    position: absolute;
    left: 0;
    right: 0;
    top: 237px;
    margin: 0;
    font-family: "Playfair Display", serif;
    font-weight: 400;
    font-size: 44px;
    line-height: 1;
    color: var(--gold);
    padding-left: 28px;
  }
  .tagline {
    position: absolute;
    left: 0;
    right: 0;
    top: 310px;
    margin: 0;
    padding-left: 28px;
    font-family: "Playfair Display", serif;
    font-style: italic;
    font-size: 25px;
    line-height: 53px;
    color: var(--sand);
  }
  .established {
    position: absolute;
    left: 0;
    right: 0;
    top: 524px;
    margin: 0;
    padding-left: 28px;
    font-family: "Work Sans", sans-serif;
    font-size: 17.5px;
    letter-spacing: 0.06em;
    color: var(--muted-gold);
  }
  .regions {
    position: absolute;
    left: 42px;
    top: 562px;
    display: flex;
    align-items: center;
    margin: 0;
    padding: 0;
    list-style: none;
    font-family: "Work Sans", sans-serif;
    font-weight: 600;
    font-size: 15.5px;
    letter-spacing: 0.05em;
    color: var(--white);
  }
  .regions li {
    height: 28px;
    line-height: 28px;
    padding: 0 15px;
    border-left: 1px solid var(--divider);
  }
  .regions li:first-child { border-left: none; padding-left: 0; }
  .regions li:last-child { padding-right: 0; }
  .company, .abn {
    position: absolute;
    left: 0;
    right: 0;
    margin: 0;
    padding-left: 28px;
    font-family: "Work Sans", sans-serif;
    font-size: 17.5px;
    letter-spacing: 0.04em;
    color: var(--muted-gold);
  }
  .company { top: 608px; }
  .abn { top: 648px; letter-spacing: 0.08em; }
  .roomscape {
    position: absolute;
    left: 534px;
    top: 60px;
    width: 606px;
    height: 624px;
    background:
      linear-gradient(180deg,
        #7c8a78 0%, #9aa393 22%, #cfc5ae 30%,
        #ddd3bc 48%, #cdbf9e 62%, #bfb18f 80%, #5b5a57 92%, #3f3f3e 100%);
  }
</style>
</head>
<body>
  <main class="home">
    <section class="brand-column">
      <h1 class="brand-name">Lune Douce</h1>
      <p class="tagline">Exquisite Luxury carpeting and area rugs<br>made from pure peruvian alpaca</p>
      <p class="established">Established in 1988</p>
      <ul class="regions">
        <li>AUSTRALIA</li>
        <li>USA</li>
        <li>EUROPE</li>
        <li>UK</li>
        <li>ASIA</li>
        <li>UAE</li>
      </ul>
      <p class="company">Lune Douce Pty Ltd</p>
      <p class="abn">ABN 31 204 519 873</p>
    </section>
    <div class="roomscape" role="img" aria-label="Bright living room with a cream sofa and cushions on a sand-toned alpaca rug with a subtle block pattern, city skyline through tall windows"></div>
  </main>
</body>
</html>
```